Ridgewell Stonecraft Construction Needs business card

Hey we are in need of business card designs. I have upload our logo as a guideline, but free feel to run with it or come up with something unique.
Pls have fun with it and be creative. the name says it all!
i will give some directions after i see a few entries..
Logo source file has been uploaded..
Hey because of the logo is so colourful already.
Can we have a few submissions with less colour.
Also we are looking for clever/hidden/descriptive business card.

```html
<!DOCTYPE html>
<html lang="en">
<head>
<meta charset="utf-8">
<title>Ridgewell Stonecraft Construction – Business Card</title>
<link rel="stylesheet" href="https://fonts.googleapis.com/css2?family=Cinzel:wght@600&display=swap">
<style>
  :root {
    --page-bg: #e9e6e2;
    --card-white: #ffffff;
    --brand-red: #ff0000;
    --brand-coral: #ff4040;
    --brand-grey: #6e7578;
    --card-edge: #5a5a5a;
    --text-light: #ffffff;
  }
  * { margin: 0; padding: 0; box-sizing: border-box; }
  html, body {
    width: 1200px;
    height: 1186px;
    overflow: hidden;
    background: var(--page-bg);
  }
  .canvas {
    position: relative;
    width: 1200px;
    height: 1186px;
  }
  .card {
    position: absolute;
    left: 230px;
    width: 740px;
    height: 420px;
    border: 1px solid var(--card-edge);
    box-shadow: 10px 14px 0 #000;
    overflow: hidden;
  }
  .card--front { top: 110px; background: var(--card-white); }
  .card--back { top: 640px; }

  .front__brand {
    height: 230px;
    display: flex;
    align-items: center;
    justify-content: center;
    gap: 18px;
    padding-top: 20px;
  }
  .brand__mark {
    width: 44px;
    height: 44px;
    background: var(--brand-red);
    flex: none;
  }
  .brand__name {
    font-family: "Cinzel", serif;
    font-weight: 600;
    color: var(--brand-grey);
    text-align: center;
    line-height: 1;
  }
  .brand__name-main {
    display: block;
    font-size: 44px;
    letter-spacing: 1px;
  }
  .brand__name-sub {
    display: block;
    font-size: 18px;
    letter-spacing: 4px;
    margin-top: 8px;
  }

  .front__contact {
    height: 190px;
    background: var(--brand-red);
    display: flex;
    flex-direction: column;
    align-items: center;
    justify-content: center;
    gap: 6px;
    font-family: "Cinzel", serif;
    font-weight: 600;
    color: var(--text-light);
    font-size: 26px;
    letter-spacing: 3px;
    line-height: 1.15;
  }

  .back__pattern {
    width: 100%;
    height: 100%;
    background: linear-gradient(135deg, var(--brand-coral) 0%, var(--brand-red) 45%, #ffd6d6 100%);
  }
</style>
</head>
<body>
  <main class="canvas">
    <section class="card card--front" aria-label="Business card front">
      <header class="front__brand">
        <span class="brand__mark" aria-hidden="true"></span>
        <h1 class="brand__name">
          <span class="brand__name-main">Ridgewell Stonecraft</span>
          <span class="brand__name-sub">Construction</span>
        </h1>
      </header>
      <address class="front__contact">
        <span class="contact__name">Proprietor Name</span>
        <span class="contact__phone">000000000</span>
        <span class="contact__email">Email</span>
        <span class="contact__address">Address</span>
      </address>
    </section>

    <section class="card card--back" aria-label="Business card back">
      <div class="back__pattern" role="img" aria-label="Checked pattern of red, coral and white squares in diagonal rows"></div>
    </section>
  </main>
</body>
</html>
```